Fitness Business Card Design Needed

We are looking for a business card design that stands out but is also simple and unique. I like the idea of on one side using the picture of myself with my logo at my feet. I love the texture on the business card so please take that into account when designing. Then on the other side having my contact details. I want it to be clean, modern, and pretty. I am open to designs that allow spot gloss or gold foiling.

Space for Name, Phone number, email, and website

```html
<!DOCTYPE html>
<html lang="en">
<head>
<meta charset="utf-8">
<title>Northfield Fitness – Business Cards</title>
<link rel="stylesheet" href="https://fonts.googleapis.com/css2?family=Exo+2:wght@400;500;700;800&display=swap">
<style>
  :root {
    --sky: #8fe2f8;
    --peach: #eebba0;
    --crimson: #cf0a22;
    --crimson-dark: #a30619;
    --gold-deep: #b8914f;
    --gold-mid: #d7ad63;
    --gold-light: #f5cd78;
    --ink: #3a3a3c;
  }
  html, body {
    margin: 0;
    padding: 0;
    width: 1200px;
    height: 1200px;
    overflow: hidden;
    background: var(--sky);
    font-family: "Exo 2", sans-serif;
  }
  .canvas {
    position: relative;
    width: 1200px;
    height: 1200px;
  }
  .card {
    position: absolute;
    top: 280px;
    width: 420px;
    height: 620px;
    box-shadow: 0 12px 30px rgba(0, 60, 90, 0.18);
  }
  .card--front { left: 150px; }
  .card--back { left: 630px; }
  .card svg { display: block; width: 100%; height: 100%; }
  .brand-name { font-family: "Exo 2", sans-serif; font-weight: 500; fill: var(--gold-light); letter-spacing: 3px; }
  .person-first { font-family: "Exo 2", sans-serif; font-weight: 800; fill: var(--ink); }
  .person-last { font-family: "Exo 2", sans-serif; font-weight: 400; fill: var(--ink); }
  .person-role { font-family: "Exo 2", sans-serif; font-weight: 500; fill: var(--ink); letter-spacing: 1px; }
  .contact-line { font-family: "Exo 2", sans-serif; font-weight: 500; fill: var(--ink); }
</style>
</head>
<body>
<main class="canvas">

  <section class="card card--front" aria-label="Business card front">
    <svg viewBox="0 0 420 620" xmlns="http://www.w3.org/2000/svg">
      <defs>
        <linearGradient id="goldFoil" x1="0" y1="0" x2="1" y2="1">
          <stop offset="0" stop-color="#c39a58"/>
          <stop offset="0.35" stop-color="#f5cd78"/>
          <stop offset="0.55" stop-color="#b8914f"/>
          <stop offset="0.8" stop-color="#e4bb6c"/>
          <stop offset="1" stop-color="#c49a5c"/>
        </linearGradient>
      </defs>
      <rect class="card-base" width="420" height="620" fill="var(--peach)"/>
      <polygon class="card-red-band" points="0,450 420,330 420,620 0,620" fill="var(--crimson)"/>
      <polygon class="portrait-panel" points="60,40 360,40 360,430 210,500 60,430" fill="url(#goldFoil)"
               role="img" aria-label="Full-length photo of the founder standing on a little sand, on a gold foil background"/>
      <polyline points="60,430 210,500 360,430" fill="none" stroke="var(--gold-deep)" stroke-width="3"/>
      <text class="brand-name" x="210" y="566" font-size="15" text-anchor="middle">NORTHFIELD FITNESS</text>
    </svg>
  </section>

  <section class="card card--back" aria-label="Business card back">
    <svg viewBox="0 0 420 620" xmlns="http://www.w3.org/2000/svg">
      <defs>
        <linearGradient id="goldFoilBack" x1="0" y1="0" x2="1" y2="1">
          <stop offset="0" stop-color="#c39a58"/>
          <stop offset="0.3" stop-color="#e8c070"/>
          <stop offset="0.5" stop-color="#b8914f"/>
          <stop offset="0.75" stop-color="#f5cd78"/>
          <stop offset="1" stop-color="#c49a5c"/>
        </linearGradient>
      </defs>
      <rect class="card-base" width="420" height="620" fill="var(--peach)"/>
      <rect class="card-gold-panel" x="40" y="230" width="340" height="330" fill="url(#goldFoilBack)"/>
      <polygon class="card-red-tab-shadow" points="65,0 355,0 355,268 210,318 65,268" fill="var(--crimson-dark)"/>
      <polygon class="card-red-tab" points="65,0 355,0 355,262 210,312 65,262" fill="var(--crimson)"/>
      <text class="brand-name" x="210" y="176" font-size="15" text-anchor="middle">NORTHFIELD FITNESS</text>

      <g class="person">
        <text x="70" y="372" font-size="36"><tspan class="person-first">DANA</tspan><tspan class="person-last"> REYES</tspan></text>
        <text class="person-role" x="72" y="398" font-size="14">Co-Founder Brand Name</text>
        <line x1="70" y1="410" x2="350" y2="410" stroke="var(--ink)" stroke-width="2"/>
        <line x1="70" y1="410" x2="130" y2="410" stroke="var(--crimson)" stroke-width="4"/>
      </g>

      <g class="contacts">
        <path d="M76 451 q0 10 10 12 l3 -3 l-3 -3 l-2 1 q-3 -2 -4 -5 l1 -2 l-3 -3 z" fill="var(--crimson)"/>
        <text class="contact-line" x="100" y="462" font-size="16">(555) 010-2486</text>

        <rect x="75" y="480" width="15" height="11" fill="var(--crimson)"/>
        <polyline points="75,480 82.5,487 90,480" fill="none" stroke="#f5cd78" stroke-width="1.2"/>
        <text class="contact-line" x="100" y="491" font-size="16">info@northfieldfit.com</text>

        <path d="M76 508 l12 5 l-5 1.5 l4 5 l-2 1.5 l-4 -5 l-3 4 z" fill="var(--crimson)"/>
        <text class="contact-line" x="100" y="520" font-size="16">www.northfieldfit.com</text>
      </g>
    </svg>
  </section>

</main>
</body>
</html>
```